Medical Waste Company with Logo

Need a business card design that targets office managers in the medical community. This card will be the front line for our sales team to market our services to the community. We would like to have email, phone number, website. Please use the logo attached to create a design that we would be proud of.

Target Market(s)

Medical Clients

Industry/Entity Type

Medical Supply

Contact Information for Business Card

Please use logo attached

Colors

Designer to choose colors to be used in the design.

Requirements
Must have
• Our logo (see attached file)
Nice to have
• Maybe a pop of some sort, raised..?

```html
<!DOCTYPE html>
<html lang="en">
<head>
<meta charset="utf-8">
<title>Borealis Clinical Waste – Business Card</title>
<link href="https://fonts.googleapis.com/css2?family=Open+Sans:wght@400;600;700&display=swap" rel="stylesheet">
<style>
  :root {
    --backdrop: #e9e7e3;
    --card: #ffffff;
    --brand-blue: #125d96;
    --charcoal: #3a3a3a;
    --ink: #333333;
    --rule: #2b2b2b;
  }
  * { margin: 0; padding: 0; box-sizing: border-box; }
  html, body {
    width: 1200px; height: 718px; overflow: hidden;
    background: var(--backdrop);
    font-family: "Open Sans", Arial, sans-serif;
  }
  .canvas { position: relative; width: 1200px; height: 718px; }
  .card {
    position: absolute; left: 75px; top: 59px;
    width: 1050px; height: 600px;
    background: var(--card);
    box-shadow: 0 6px 22px rgba(0,0,0,.18);
    overflow: hidden;
  }
  .brand {
    position: absolute; left: 70px; top: 200px;
    display: flex; align-items: center; gap: 16px;
  }
  .brand-mark { width: 26px; height: 26px; background: var(--brand-blue); }
  .brand-name {
    color: var(--brand-blue); font-weight: 700; font-size: 34px;
    letter-spacing: .5px; text-transform: uppercase; line-height: 1.15;
  }
  .divider {
    position: absolute; top: 330px; height: 1.5px; background: var(--rule);
  }
  .divider--left { left: 330px; width: 330px; }
  .divider--right { left: 930px; width: 70px; top: 60px; }
  .person { position: absolute; left: 672px; top: 300px; }
  .person-name {
    color: var(--brand-blue); font-weight: 700; font-size: 38px;
    letter-spacing: .5px; line-height: 1;
  }
  .person-role { color: var(--ink); font-size: 21px; margin-top: 10px; }
  .contacts {
    position: absolute; left: 395px; top: 380px;
    list-style: none; display: flex; flex-direction: column; gap: 14px;
  }
  .contact { display: flex; align-items: center; gap: 18px; color: var(--ink); font-size: 25px; }
  .contact svg { width: 24px; height: 24px; flex: none; }
  .band { position: absolute; bottom: 0; height: 56px; }
  .band--blue { left: 0; width: 720px; background: var(--brand-blue); }
  .band--charcoal { left: 720px; right: 0; height: 64px; background: var(--charcoal); }
</style>
</head>
<body>
<main class="canvas">
  <section class="card">
    <div class="brand">
      <span class="brand-mark"></span>
      <span class="brand-name">Borealis Clinical<br>Waste</span>
    </div>

    <div class="divider divider--left"></div>

    <div class="person">
      <p class="person-name">MARA KELLEN</p>
      <p class="person-role">Managing Director</p>
    </div>

    <ul class="contacts">
      <li class="contact">
        <svg viewBox="0 0 24 24" aria-hidden="true"><rect x="2" y="5" width="20" height="14" rx="2" fill="#125d96"/><path d="M3 6l9 7 9-7" fill="none" stroke="#fff" stroke-width="1.8"/></svg>
        m.kellen@kestrelnet.com
      </li>
      <li class="contact">
        <svg viewBox="0 0 24 24" aria-hidden="true"><path d="M6.6 10.8a15 15 0 006.6 6.6l2.2-2.2a1 1 0 011-.25 11.4 11.4 0 003.6.57 1 1 0 011 1V20a1 1 0 01-1 1A17 17 0 013 4a1 1 0 011-1h3.5a1 1 0 011 1c0 1.25.2 2.45.57 3.6a1 1 0 01-.25 1z" fill="#125d96"/></svg>
        555-014-2387
      </li>
      <li class="contact">
        <svg viewBox="0 0 24 24" aria-hidden="true"><circle cx="12" cy="12" r="10" fill="#125d96"/><g fill="none" stroke="#fff" stroke-width="1.3"><ellipse cx="12" cy="12" rx="4" ry="10"/><path d="M2 12h20M4 7h16M4 17h16"/></g></svg>
        www.kestrelnet.com
      </li>
    </ul>

    <div class="band band--blue"></div>
    <div class="band band--charcoal"></div>
  </section>
</main>
</body>
</html>
```